Black Granite Web Design Project

We are looking for a design for a new company that will be selling Black Granite slabs and tiles. We will be selling to both end-consumers and granite installers. We have already settled on a logo and hopefully this will give an idea of what we like in our designs. We are not going to be selling online but want people to call us so the site is basically an enhanced business card. We will be focusing a lot on SEO so the design will have to keep that in mind.

We would like to keep the design in 1024x768 to make it easily view-able on all devices.

Regarding navigation there should only be a few sub-pages, like "Granite Slabs", "Granite Tiles", "Delivery", "Contact"

Aside from that we are open to designs. One idea we did have was to personalize the site and have a person there somehow to represent the company, making the user feel there are real people behind this site. This is just an idea and not a must.

The name of the company and site is "Silver Brook Petrano"

Thanks
Updates

Hello All,

Thanks for the great designs. There are some good looking designs that show beautiful kitchens but this site is made for the granite installers and not the retail consumers. So in order not to to confuse the buyers I would like to keep this as much about the raw products as possible. The raw products being the granite slabs, thereby making it obvious we don't sell granite counter tops. 

This design will really be the identity of this company so it is important we get the right message across on this index page and that this page is as complete as possible.

Again, thanks for all the work being put into this.

Target Market(s)

The target audience is granite installers or companies that would with granite slabs.

Industry/Entity Type

Business

```html
<!DOCTYPE html>
<html lang="en">
<head>
<meta charset="utf-8">
<title>Silver Brook Petrano</title>
<link href="https://fonts.googleapis.com/css2?family=PT+Sans:wght@400;700&family=PT+Sans+Narrow:wght@400;700&display=swap" rel="stylesheet">
<style>
:root{
  --page:#2b2b2b;
  --panel:#f7f7f7;
  --white:#ffffff;
  --line:#dcdcdc;
  --green:#4b7a2c;
  --green-dark:#30491f;
  --green-light:#5f8a44;
  --dark:#353535;
  --darker:#222;
  --text:#444;
  --muted:#777;
}
*{margin:0;padding:0;box-sizing:border-box}
html,body{width:920px;height:1200px;overflow:hidden}
body{background:var(--page);font-family:"PT Sans",sans-serif;color:var(--text);position:relative}
.abs{position:absolute}
.narrow{font-family:"PT Sans Narrow",sans-serif}

/* header */
.header{left:67px;top:16px;width:784px;height:130px;background:linear-gradient(#fff,#f1f1f1);border-radius:2px}
.brand{left:10px;top:38px;display:flex;align-items:center;gap:8px;font-family:"PT Sans Narrow",sans-serif;font-weight:700;font-size:26px;color:var(--darker);letter-spacing:-.3px}
.brand .mark{width:18px;height:18px;background:var(--green)}
.cart{left:415px;top:14px;width:192px;height:60px;border:1px solid var(--line);background:#f4f4f4;border-radius:2px}
.cart .title{left:19px;top:10px;font-size:12px;font-weight:700;color:var(--muted)}
.cart svg{left:26px;top:27px}
.cart .info{left:88px;top:8px;font-size:9.5px;line-height:17.5px;color:#555}
.cart .info .links{color:var(--muted)}
.search{left:615px;top:14px;width:162px;height:22px;border:1px solid #ccc;background:#fff;font-size:10px;color:#888;padding:5px 9px}
.search svg{position:absolute;right:6px;top:3px}
.ship{left:615px;top:42px;width:162px;height:32px;background:linear-gradient(#555,#2e2e2e);color:#eee;font-family:"PT Sans Narrow",sans-serif;font-weight:700;font-size:13.5px;display:flex;align-items:center;gap:9px;padding-left:18px}
.nav{left:347px;top:86px;height:31px;width:430px;background:#ececec;display:flex}
.nav a{font-family:"PT Sans Narrow",sans-serif;font-size:14.5px;color:#444;text-decoration:none;display:flex;align-items:center;justify-content:center}
.nav a.active{background:#3d3d3d;color:#fff;border-bottom:2px solid var(--green)}

/* slider */
.slider{left:67px;top:154px;width:784px;height:248px;background:#555;border-radius:2px}
.slide{left:6px;top:4px;width:773px;height:240px;background:linear-gradient(90deg,#3a332e 0%,#5e5a55 35%,#2e2a28 55%,#8b8b8b 75%,#bdb7ac 100%)}
.caption{left:93px;top:358px;font-family:"PT Sans Narrow",sans-serif;font-weight:700;font-size:19px;color:#ddd;letter-spacing:-.3px;text-shadow:0 1px 2px #000}
.arrow{top:359px;width:23px;height:23px;border-radius:50%;background:#eee;border:2px solid #555;display:flex;align-items:center;justify-content:center}

/* main */
.main{left:67px;top:411px;width:784px;height:669px;background:var(--panel);border-radius:2px}
.cat-head{left:79px;top:425px;width:182px;height:37px;background:linear-gradient(var(--green-light),var(--green-dark));color:#fff;font-family:"PT Sans Narrow",sans-serif;font-weight:700;font-size:16px;padding:9px 11px;border-radius:2px}
.cat-list{left:81px;top:462px;width:180px;height:380px;background:#f1f1f1;border:1px solid #e2e2e2;list-style:none;padding-top:5px}
.cat-list li{height:30.4px;display:flex;align-items:center;font-family:"PT Sans Narrow",sans-serif;font-size:15.5px;color:var(--green)}
.cat-list li::before{content:"›";color:#888;font-size:13px;width:30px;padding-left:11px;border-right:0}
.gallery{left:80px;top:850px;width:180px;height:186px;background:linear-gradient(135deg,#2a2a2a,#111 40%,#3a3a3a 70%,#1b1b1b)}
.gallery .g-title{left:15px;top:16px;font-family:"PT Sans Narrow",sans-serif;font-weight:700;font-size:17.5px;color:#fff}
.gallery .grid{position:absolute;left:0;top:59px;width:180px;height:127px;background:
 linear-gradient(90deg,transparent 59px,#555 59px,#555 60px,transparent 60px,transparent 120px,#555 120px,#555 121px,transparent 121px),
 linear-gradient(transparent 62px,#555 62px,#555 63px,transparent 63px)}

.welcome{left:280px;top:427px;font-family:"PT Sans Narrow",sans-serif;font-weight:700;font-size:20px;color:var(--green)}
.intro{left:280px;top:458px;width:558px;font-size:10.9px;line-height:17.6px;text-align:justify;color:#555}
.divider{left:280px;top:563px;width:564px;height:1px;background:var(--line)}
.tab{top:582px;height:30px;width:59px;display:flex;align-items:center;justify-content:center;color:#fff;font-family:"PT Sans Narrow",sans-serif;font-size:14.5px}
.tab.slabs{left:280px;background:var(--green);border-bottom:2px solid var(--green-dark)}
.tab.tiles{left:341px;background:#3d3d3d;border-bottom:2px solid #222}
.flabel{top:590px;font-size:11px;color:#444}
.select{top:584px;height:26px;border:1px solid #ccc;background:#fff;font-size:10px;color:#777;padding:6px 9px}
.select::after{content:"";position:absolute;right:7px;top:10px;border:4px solid transparent;border-top:5px solid #888}
.swatch{display:block;width:20px;height:14px;background:#555;margin-top:-2px}

.card{width:178px;height:91px;background:#fff;border:1px solid #e4e4e4}
.card .thumb{position:absolute;left:9px;top:9px;width:72px;height:72px;border:3px solid #d4d4d4}
.card .name{position:absolute;left:90px;top:9px;font-family:"PT Sans Narrow",sans-serif;font-weight:700;font-size:12px;color:var(--green)}
.card .dim{position:absolute;left:90px;top:26px;font-family:"PT Sans Narrow",sans-serif;font-size:11px;color:var(--muted)}
.card .order{position:absolute;left:91px;top:49px;width:79px;height:29px;background:linear-gradient(#444,#1f1f1f);border-radius:2px;color:#fff;font-family:"PT Sans Narrow",sans-serif;font-weight:700;font-size:11px;display:flex;align-items:center;gap:5px;padding-left:8px}

.pager{left:744px;top:1050px;display:flex;gap:2px}
.pager span{width:18px;height:17px;background:#ddd;border:1px solid #ccc;font-size:7px;color:#999;display:flex;align-items:center;justify-content:center}
.pager span.on{background:#777;color:#fff;border-color:#666}

/* footer */
.foot-links{left:68px;top:1102px;font-family:"PT Sans Narrow",sans-serif;font-size:12px;color:#ddd;word-spacing:2px}
.copy{left:68px;top:1128px;font-family:"PT Sans Narrow",sans-serif;font-size:12px;color:#ddd}
.social{top:1156px;width:20px;height:20px;border-radius:50%;background:#777}
.foot-brand{left:697px;top:1150px;font-family:"PT Sans Narrow",sans-serif;font-weight:700;font-size:18px;color:#ddd;display:flex;align-items:center;gap:6px}
.foot-brand .mark{width:13px;height:13px;background:#ddd}
</style>
</head>
<body>

<header class="abs header">
  <div class="abs brand"><span class="mark"></span>Silver Brook Petrano</div>

  <div class="abs cart">
    <div class="abs title">My Cart</div>
    <svg class="abs" width="30" height="26" viewBox="0 0 30 26"><path d="M1 3h5l4 14h14l3-10H8" fill="none" stroke="#888" stroke-width="2.2"/><circle cx="12" cy="22" r="2.3" fill="#888"/><circle cx="22" cy="22" r="2.3" fill="#888"/></svg>
    <div class="abs info">(0) items in your cart<br>Total - $ 00.00<br><span class="links">My Account &nbsp;|&nbsp; My List</span></div>
  </div>

  <div class="abs search">Search
    <svg width="16" height="16" viewBox="0 0 16 16"><circle cx="6.5" cy="6.5" r="4.5" fill="none" stroke="#666" stroke-width="2.2"/><path d="M10 10l4.5 4.5" stroke="#666" stroke-width="2.6"/></svg>
  </div>
  <div class="abs ship">
    <svg width="22" height="15" viewBox="0 0 22 15"><rect x="6" y="1" width="15" height="9" fill="#bbb"/><path d="M1 5h5v5H1z" fill="#bbb"/><circle cx="5" cy="12" r="2.2" fill="#bbb"/><circle cx="17" cy="12" r="2.2" fill="#bbb"/></svg>
    SHIPPING DETAILS
  </div>

  <nav class="abs nav">
    <a class="active" href="#" style="width:59px">HOME</a>
    <a href="#" style="width:109px">GRANIT SLABS</a>
    <a href="#" style="width:103px">GRANITE TILES</a>
    <a href="#" style="width:82px">DELIVERY</a>
    <a href="#" style="width:77px">CONTACT</a>
  </nav>
</header>

<section class="abs slider">
  <div class="abs slide" role="img" aria-label="Interior photo of a kitchen and a bathroom vanity with granite countertops"></div>
</section>
<div class="abs caption">DONEC ID TRISTIQUE EST, UT COMMODO TURPIS</div>
<div class="abs arrow" style="left:779px"><svg width="8" height="10" viewBox="0 0 8 10"><path d="M6 1L2 5l4 4" fill="none" stroke="#333" stroke-width="2"/></svg></div>
<div class="abs arrow" style="left:804px"><svg width="8" height="10" viewBox="0 0 8 10"><path d="M2 1l4 4-4 4" fill="none" stroke="#333" stroke-width="2"/></svg></div>

<main class="abs main"></main>

<aside>
  <div class="abs cat-head">SLABS CATEGORIES</div>
  <ul class="abs cat-list">
    <li>Granite Slabs</li><li>Marble Slabs</li><li>Soapstone &amp; Slate</li><li>Crystaline Stone</li>
    <li>Granite Slabs</li><li>Marble Slabs</li><li>Soapstone &amp; Slate</li><li>Crystaline Stone</li>
    <li>Granite Slabs</li><li>Marble Slabs</li><li>Soapstone &amp; Slate</li><li>Crystaline Stone</li>
  </ul>
  <div class="abs gallery" role="img" aria-label="Featured gallery of dark granite tile samples">
    <div class="abs g-title">FEATURED GALLERY</div>
    <div class="grid"></div>
  </div>
</aside>

<h1 class="abs welcome">WELCOME TO SILVER BROOK PETRANO</h1>
<p class="abs intro">Donec consequat tincidunt nisl, eu tincidunt mauris imperdiet at. Nam scelerisque rhoncus leo, a bibendum ipsum placerat a. Curabitur massa tortor, faucibus quis dui eu, consectetur vehicula diam. Aliquam hendrerit ligula non tortor blandit, at convallis nunc fermentum. Integer sodales tristique tincidunt. Phasellus sed sapien sed urna aliquet consequat. Vivamus lacinia lacus sapien, at semper nisl pulvinar at. Vivamus scelerisque lorem risus, a sollicitudin nibh convallis nec. Quisque vehicula eu nulla id interdum. Nam eget eros blandit, accumsan tortor quis, scelerisque odio.</p>
<div class="abs divider"></div>

<div class="abs tab slabs">SLABS</div>
<div class="abs tab tiles">TILES</div>
<div class="abs flabel" style="left:427px">Color :</div>
<div class="abs select" style="left:464px;width:50px"><span class="swatch"></span></div>
<div class="abs flabel" style="left:531px">Dimension :</div>
<div class="abs select" style="left:592px;width:50px">00</div>
<div class="abs flabel" style="left:647px">X</div>
<div class="abs select" style="left:658px;width:50px">00</div>
<div class="abs flabel" style="left:726px">Thickness :</div>
<div class="abs select" style="left:784px;width:60px">0cm</div>

<!-- product grid -->
<div class="abs card" style="left:279px;top:634px"><div class="thumb" role="img" aria-label="Black granite sample" style="background:#1c1c1c"></div><div class="name">Slab Name</div><div class="dim">Slab Dimension</div><div class="order"><svg width="14" height="12" viewBox="0 0 14 12"><path d="M0 1h3l2 7h7l1.5-5H4" fill="none" stroke="#fff" stroke-width="1.8"/><circle cx="6" cy="10.5" r="1.3" fill="#fff"/><circle cx="11" cy="10.5" r="1.3" fill="#fff"/></svg>Order Now</div></div>
<div class="abs card" style="left:473px;top:634px"><div class="thumb" role="img" aria-label="Dark blue granite sample" style="background:#1f1f2a"></div><div class="name">Slab Name</div><div class="dim">Slab Dimension</div><div class="order"><svg width="14" height="12" viewBox="0 0 14 12"><path d="M0 1h3l2 7h7l1.5-5H4" fill="none" stroke="#fff" stroke-width="1.8"/><circle cx="6" cy="10.5" r="1.3" fill="#fff"/><circle cx="11" cy="10.5" r="1.3" fill="#fff"/></svg>Order Now</div></div>
<div class="abs card" style="left:666px;top:634px"><div class="thumb" role="img" aria-label="Dark brown granite sample" style="background:#241d18"></div><div class="name">Slab Name</div><div class="dim">Slab Dimension</div><div class="order"><svg width="14" height="12" viewBox="0 0 14 12"><path d="M0 1h3l2 7h7l1.5-5H4" fill="none" stroke="#fff" stroke-width="1.8"/><circle cx="6" cy="10.5" r="1.3" fill="#fff"/><circle cx="11" cy="10.5" r="1.3" fill="#fff"/></svg>Order Now</div></div>

<div class="abs card" style="left:279px;top:738px"><div class="thumb" role="img" aria-label="Black and white speckled granite sample" style="background:#525252"></div><div class="name">Slab Name</div><div class="dim">Slab Dimension</div><div class="order"><svg width="14" height="12" viewBox="0 0 14 12"><path d="M0 1h3l2 7h7l1.5-5H4" fill="none" stroke="#fff" stroke-width="1.8"/><circle cx="6" cy="10.5" r="1.3" fill="#fff"/><circle cx="11" cy="10.5" r="1.3" fill="#fff"/></svg>Order Now</div></div>
<div class="abs card" style="left:473px;top:738px"><div class="thumb" role="img" aria-label="Light grey granite sample" style="background:#a3a3a3"></div><div class="name">Slab Name</div><div class="dim">Slab Dimension</div><div class="order"><svg width="14" height="12" viewBox="0 0 14 12"><path d="M0 1h3l2 7h7l1.5-5H4" fill="none" stroke="#fff" stroke-width="1.8"/><circle cx="6" cy="10.5" r="1.3" fill="#fff"/><circle cx="11" cy="10.5" r="1.3" fill="#fff"/></svg>Order Now</div></div>
<div class="abs card" style="left:666px;top:738px"><div class="thumb" role="img" aria-label="Grey granite sample" style="background:#6e6e6e"></div><div class="name">Slab Name</div><div class="dim">Slab Dimension</div><div class="order"><svg width="14" height="12" viewBox="0 0 14 12"><path d="M0 1h3l2 7h7l1.5-5H4" fill="none" stroke="#fff" stroke-width="1.8"/><circle cx="6" cy="10.5" r="1.3" fill="#fff"/><circle cx="11" cy="10.5" r="1.3" fill="#fff"/></svg>Order Now</div></div>

<div class="abs card" style="left:279px;top:842px"><div class="thumb" role="img" aria-label="Grey speckled granite sample" style="background:#8c8c8c"></div><div class="name">Slab Name</div><div class="dim">Slab Dimension</div><div class="order"><svg width="14" height="12" viewBox="0 0 14 12"><path d="M0 1h3l2 7h7l1.5-5H4" fill="none" stroke="#fff" stroke-width="1.8"/><circle cx="6" cy="10.5" r="1.3" fill="#fff"/><circle cx="11" cy="10.5" r="1.3" fill="#fff"/></svg>Order Now</div></div>
<div class="abs card" style="left:473px;top:842px"><div class="thumb" role="img" aria-label="Medium grey granite sample" style="background:#797979"></div><div class="name">Slab Name</div><div class="dim">Slab Dimension</div><div class="order"><svg width="14" height="12" viewBox="0 0 14 12"><path d="M0 1h3l2 7h7l1.5-5H4" fill="none" stroke="#fff" stroke-width="1.8"/><circle cx="6" cy="10.5" r="1.3" fill="#fff"/><circle cx="11" cy="10.5" r="1.3" fill="#fff"/></svg>Order Now</div></div>
<div class="abs card" style="left:666px;top:842px"><div class="thumb" role="img" aria-label="Beige and grey veined granite sample" style="background:#9b9a8d"></div><div class="name">Slab Name</div><div class="dim">Slab Dimension</div><div class="order"><svg width="14" height="12" viewBox="0 0 14 12"><path d="M0 1h3l2 7h7l1.5-5H4" fill="none" stroke="#fff" stroke-width="1.8"/><circle cx="6" cy="10.5" r="1.3" fill="#fff"/><circle cx="11" cy="10.5" r="1.3" fill="#fff"/></svg>Order Now</div></div>

<div class="abs card" style="left:279px;top:946px"><div class="thumb" role="img" aria-label="Olive green stone sample" style="background:#878269"></div><div class="name">Slab Name</div><div class="dim">Slab Dimension</div><div class="order"><svg width="14" height="12" viewBox="0 0 14 12"><path d="M0 1h3l2 7h7l1.5-5H4" fill="none" stroke="#fff" stroke-width="1.8"/><circle cx="6" cy="10.5" r="1.3" fill="#fff"/><circle cx="11" cy="10.5" r="1.3" fill="#fff"/></svg>Order Now</div></div>
<div class="abs card" style="left:473px;top:946px"><div class="thumb" role="img" aria-label="Red granite sample" style="background:#6a3a2b"></div><div class="name">Slab Name</div><div class="dim">Slab Dimension</div><div class="order"><svg width="14" height="12" viewBox="0 0 14 12"><path d="M0 1h3l2 7h7l1.5-5H4" fill="none" stroke="#fff" stroke-width="1.8"/><circle cx="6" cy="10.5" r="1.3" fill="#fff"/><circle cx="11" cy="10.5" r="1.3" fill="#fff"/></svg>Order Now</div></div>
<div class="abs card" style="left:666px;top:946px"><div class="thumb" role="img" aria-label="Brown banded granite sample" style="background:#5b4239"></div><div class="name">Slab Name</div><div class="dim">Slab Dimension</div><div class="order"><svg width="14" height="12" viewBox="0 0 14 12"><path d="M0 1h3l2 7h7l1.5-5H4" fill="none" stroke="#fff" stroke-width="1.8"/><circle cx="6" cy="10.5" r="1.3" fill="#fff"/><circle cx="11" cy="10.5" r="1.3" fill="#fff"/></svg>Order Now</div></div>

<div class="abs pager"><span class="on">1</span><span>2</span><span>3</span><span>4</span><span>5</span></div>

<footer>
  <div class="abs foot-links">Home &nbsp;|&nbsp; Granit Slabs &nbsp;|&nbsp; Granite Tiles &nbsp;|&nbsp; Delivery &nbsp;|&nbsp; Contact</div>
  <div class="abs copy">Copyright &copy; 2013 &nbsp;Silver Brook Petrano. &nbsp;&nbsp;All rights reserved.</div>
  <div class="abs social" style="left:68px"></div>
  <div class="abs social" style="left:95px"></div>
  <div class="abs social" style="left:122px"></div>
  <div class="abs social" style="left:148px;display:flex;align-items:center;justify-content:center"><svg width="11" height="8" viewBox="0 0 11 8"><rect x=".5" y=".5" width="10" height="7" fill="none" stroke="#eee"/><path d="M.5 .5l5 4 5-4" fill="none" stroke="#eee"/></svg></div>
  <div class="abs foot-brand"><span class="mark"></span>Silver Brook Petrano</div>
</footer>

</body>
</html>
```